Prescripton Pad for Mental health professionals and life wellness coaches

I need a note pad designed for therapist and coaches that will allow us to write our client homework just like a doctor would write out a prescription for medication.(i.e read for chapter of book, or 30 minutes of mediation a day, etc.). I would like to see sections for stuff to ponder, as well as action to take. Something that has the seriousness of a doctor pad but also some sleep professional twist to it. I would like for these to be sold where businesses can add in their own names and logos at the top.

Target Market(s)

Mental Health Professionals, Psychiatrist, Life coaches, Wellness Coaches

Industry/Entity Type

Mental Health

Font styles to use
Script

Requirements
Must have
• Space for individuals to add in their own name a logos
• Look of a prescription pad from the doctor
• Some sleek, unique aspect to it
Nice to have
• Section with boxed that can be checked such as :mindfulness, Meditation, cardio, strength training, massage, date night, Sleep _ hours

```html
<!DOCTYPE html>
<html lang="en">
<head>
<meta charset="utf-8">
<title>Therapy Prescription Pad</title>
<link href="https://fonts.googleapis.com/css2?family=Open+Sans:wght@400;600;700&display=swap" rel="stylesheet">
<style>
:root{
  --navy:#0f4873;
  --gold:#f7c51a;
  --ink:#3a3a3a;
  --line:#555;
  --paper:#ffffff;
  --stage:#ebe6de;
  --mist:#a9bfd0;
}
*{box-sizing:border-box;margin:0;padding:0}
html,body{width:1200px;height:1200px;overflow:hidden}
body{background:var(--stage);font-family:"Open Sans",sans-serif;color:var(--ink);position:relative}
.pad{position:absolute;width:532px;height:688px;background:var(--paper);box-shadow:0 3px 10px rgba(0,0,0,.25);overflow:hidden}
.pad--classic{left:52px;top:257px}
.pad--compact{left:612px;top:256px;width:534px;height:691px}
.pad__header{position:absolute;left:0;top:0;width:100%;height:60px}
.brand{position:absolute;left:36px;top:60px;display:flex;align-items:center;gap:7px}
.brand__dot{width:14px;height:14px;border-radius:50%;background:var(--navy);flex:none}
.brand__name{font-weight:700;color:var(--navy);font-size:14px;line-height:16px;white-space:nowrap}
.brand__address{position:absolute;left:40px;top:99px;font-size:6px;line-height:7px;color:var(--navy);white-space:nowrap}
.client-fields{position:absolute;left:295px;top:45px;font-size:12.5px;line-height:17.5px}
.client-fields li{list-style:none;display:flex}
.client-fields span{width:106px}
.pad__title{position:absolute;left:0;right:0;top:118px;text-align:center;font-size:19.5px;font-weight:600}
.section-label{position:absolute;left:42px;font-size:14px;font-weight:600}
.write-box{position:absolute;left:41px;width:454px;border:1px solid #777;border-radius:3px}
.goals-label{top:140px}
.goals-box{top:162px;height:95px}
.order-label{top:268px}
.orders{position:absolute;left:41px;top:294px;width:460px;display:grid;grid-template-columns:284px 1fr;grid-auto-flow:column;grid-template-rows:repeat(5,18.5px);font-size:10px;font-weight:600}
.orders li{list-style:none;display:flex;align-items:center;gap:6px}
.orders li::before{content:"";width:9px;height:9px;border:1px solid #555}
.blank{display:inline-block;width:38px;border-bottom:1px solid var(--line);margin:0 4px}
.blank--wide{width:70px}
.comments-label{top:394px}
.comments-box{top:418px;height:175px}
.signature{position:absolute;left:61px;top:616px;font-size:14px;font-weight:600;display:flex;align-items:flex-end;gap:14px}
.signature i{display:block;width:142px;border-bottom:1px solid var(--line);margin-bottom:4px}
.lighthouse-art{position:absolute;left:426px;top:538px;width:94px;height:110px;background:linear-gradient(180deg,#f4e6a0 0%,var(--mist) 35%,#c9d8e3 100%);border-radius:40px 40px 6px 6px;opacity:.85}
.pad__footer{position:absolute;left:0;bottom:0;width:100%;height:37px;background:var(--navy);color:#fff;font-size:9.5px;text-align:center;padding-top:6px;line-height:13px}
.pad--compact .brand{top:54px}
.pad--compact .pad__title{top:120px}
.pad--compact .goals-label{top:141px}
.pad--compact .goals-box{top:163px}
.pad--compact .order-label{top:270px}
.pad--compact .orders{top:295px;grid-template-columns:286px 1fr}
.pad--compact .comments-label{top:397px}
.pad--compact .comments-box{top:421px;height:185px}
.pad--compact .signature{left:61px;top:629px}
.pad--compact .lighthouse-art{left:435px;top:550px}
.pad--compact .client-fields{left:338px;top:50px}
.pad--compact .pad__footer{height:30px;padding-top:8px;font-weight:700;letter-spacing:.8px}
</style>
</head>
<body>

<section class="pad pad--classic">
  <svg class="pad__header" viewBox="0 0 532 60" preserveAspectRatio="none">
    <path d="M0 0H532V48Q280 0 0 55Z" fill="#0f4873"/>
    <path d="M0 53Q280 4 532 44V50Q280 8 0 58Z" fill="#f7c51a"/>
  </svg>
  <div class="brand"><span class="brand__dot"></span><span class="brand__name">Harborlight<br>Family Counseling</span></div>
  <ul class="client-fields">
    <li><span>Patient</span>:</li>
    <li><span>Therapist/coach</span>:</li>
    <li><span>Follow up date</span>:</li>
  </ul>
  <h1 class="pad__title">Therapy Prescription</h1>
  <h2 class="section-label goals-label">Goals</h2>
  <div class="write-box goals-box"></div>
  <h2 class="section-label order-label">Order</h2>
  <ul class="orders">
    <li>Sleep<i class="blank"></i>hrs/day</li>
    <li>Water Intake<i class="blank" style="width:46px"></i>ounces</li>
    <li>Exercise</li>
    <li>Nutrition</li>
    <li>Meditation</li>
    <li>Read<i class="blank blank--wide"></i></li>
    <li>Breathing Exercises</li>
    <li>Mindfulness</li>
    <li>Others :</li>
  </ul>
  <h2 class="section-label comments-label">Additional comments</h2>
  <div class="write-box comments-box"></div>
  <div class="signature">Therapist/coach Signature <i></i></div>
  <div class="lighthouse-art" role="img" aria-label="Lighthouse on ocean waves illustration"></div>
  <footer class="pad__footer">Harborlight Family Counseling. 418 Bayview Road Suite B Millbrook Texas 77390<br>www.harborlightfamilies.com</footer>
</section>

<section class="pad pad--compact">
  <svg class="pad__header" viewBox="0 0 534 60" preserveAspectRatio="none">
    <path d="M0 0H534V48Q280 0 0 55Z" fill="#0f4873"/>
    <path d="M0 53Q280 4 534 44V50Q280 8 0 58Z" fill="#f7c51a"/>
  </svg>
  <div class="brand"><span class="brand__dot"></span><span class="brand__name">Harborlight<br>Family Counseling</span></div>
  <p class="brand__address">418 Bayview Road Suite B Millbrook Texas 77390</p>
  <ul class="client-fields">
    <li><span>Patient</span>:</li>
    <li><span>Therapist/coach</span>:</li>
    <li><span>Follow up date</span>:</li>
  </ul>
  <h1 class="pad__title">Therapy Prescription</h1>
  <h2 class="section-label goals-label">Goals</h2>
  <div class="write-box goals-box" style="width:457px"></div>
  <h2 class="section-label order-label">Order</h2>
  <ul class="orders">
    <li>Sleep<i class="blank"></i>hrs/day</li>
    <li>Water Intake<i class="blank" style="width:46px"></i>ounces</li>
    <li>Exercise</li>
    <li>Nutrition</li>
    <li>Meditation</li>
    <li>Read<i class="blank blank--wide"></i></li>
    <li>Breathing Exercises</li>
    <li>Mindfulness</li>
    <li>Others :</li>
  </ul>
  <h2 class="section-label comments-label">Additional comments</h2>
  <div class="write-box comments-box" style="width:457px"></div>
  <div class="signature">Therapist/coach Signature <i></i></div>
  <div class="lighthouse-art" role="img" aria-label="Lighthouse on ocean waves illustration"></div>
  <footer class="pad__footer">www.harborlightfamilies.com</footer>
</section>

</body>
</html>
```